Iconic Cool Labels for Amazing Coffee

I'm back again after a very successful logo design project, now looking for label designs!

NOTEs:

IF YOU SUBMIT A DESIGN YOU WILL DEFINITELY RECEIVE FEEDBACK. I think it's rude not to respond when somebody takes the time to devote their time and talent to a project like this.

THIS BRIEF IS LONG. Out of respect for you, the designers. I've put a lot of time into this to give you as much understanding as I can. I think if you are going to invest your time it is only right and proper that I do the same. So please don't be put off by the length - it is intended to save you time and energy.

THE BRIEF

We are launching a coffee website called Brewvantia aimed at those who really care about coffee and have a passion for getting the very best out of it. So far, we have a great logo (attached), we have the website under construction and with the look and feel decided.

We are not a mass market player - instead we are more like an online boutique. But, we are starting out and need to look chic in a way that doesn't involve large investments. So, our coffee will be packaged in bags (1kg and 250g) with brown paper exteriors (brown kraft) onto which we'll put self adhesive labels.This is where we need your help.

THE TASK
- Create the 2 "master" labels for the front of the bags
- Create the variety labels that go either on or somewhere around the master label
- Create a small label for the back of the bag that contains the required regulatory information

There are 2 "families" - each requiring a family label. They are our blends (there are 7 of these), our single origin coffees (there are 3 of these) and the fair trade organic.

MASTER LABELS - In my mind the main focus of this brief
For the front of the bag there will be a master label for each of the 2 families, with another self-adhesive label placed either on top of the master label or adjacent to it. The exception being the free trade organic - there is only one of these, so no over labelling required.

The master labels are the main game here. They need to be distinctive and tasteful. They should look "chic" but not "try hard". They should be different to each other yet clearly part of the same house.

Both master labels MUST include the Brewvantia logo (supplied) and must also include a small Tessaro logo somewhere. Tessaro is our roaster. Perhaps it might be "Proudly roasted by (Tessaro logo)", or something like that.

The master labels are needed in each of the 1kg and 250g sizes and should have the size displayed as a part of the label.

The 2 master labels are:
Blends - these are beans from multiple origins and are typically used for espresso, late etc. I'd prefer that the label doesn't say "blends".

Single Origin - these are coffees from a single place in the world. They are for enthusiasts who want to explore the nuance and subtlety of a single region. Rather than be made in an espresso machine (although they can be) siphons are where these truly come in to their own.

VARIETY LABEL
These will either be stuck in a designated space on the MASTER LABEL or will be stuck somewhere else on the usable area. There are 7 of these in the blends family and 3 in the single origins family. They may be all very similar in look and feel or they may be variations within a theme. What do you think they should be?

You may decide to make them look similar of different. You might have groups - e.g. the first four, the free trade organics and the decafs. (Though if you do please don't do the cliched thing and make the decafs blue!)

Our Varieties are:
BLENDS
The Keystone
The Devotee
The Sybarite
The Reveller
Free Trade Organic
Swiss Decafeinated
Mexican Mountain Decafeinated

SINGLE ORIGIN
Ethiopian Garsu
Costa Rica El Pinar
Nicaraguan Tolvanera Superior

COMPLIANCE LABEL
This is a small label to go onto the back of the bag for all of our coffees. It contains all of the regulatory and compliance information. I'd like this to be small and reasonably unobtrusive, but clearly from the same "stable" as the other labels. This should be a regular shape so it's easy and quick to stick on, but not necessarily a rectangle - you pick.

It should contain:

Brewvantia
PO Box 4736
Larvik VIC 3902
www.brewvantia-example.com.au

Roasted, Blended & Packed in Australia
from Imported Beans

Store away from sunlight in a cool dry place

TECHNICAL DETAILS
The usable areas are (in portrait format)
1kg - 180mm high by 100mm wide
250g - 140mm high by 70mm wide

How much of this space you use and how you use it is up to you. My ingoing feeling is that using all of the available space would make it look "mass market" rather than premium. On the front, maybe there are a couple of small labels that are spaced, maybe there's one big label with an over sticker. I don't want to constrain you too much in this regard - except to say that unusual shapes like stars may be both slow and awkward to put onto the bags

THE CREATIVE SIDE
This is where you come in...
- Do you use all the space of just some of it (my guess is the latter)?
- One master on the front with an oversticker for variety or 2 separate labels?
- Rectangular labels or another shape (not jagged shapes please - too hard to stick evenly)
- Does the label contain, just words or does it have images, photos etc?
- Are the variety labels all similar or do they have a different look and feel?

ATTACHMENTS
- Brewvantia logo pack in zip file
- Tessaro logo
- Some photos I shared for the logo brief as examples
Updates

All, 

The files I thought I'd attached didn't get there the first time. I think I've corrected that now. Sorry for any hassle caused.

Cheers,
Joe

Target Market(s)

Our target customers have one thing in common - they are passionate about excellent coffee. While they come from all walks of life the image in my head is of young professionals that wear designer clothes - lots of black - and are passionate about design. They aspire to have Halvor furniture and care passionately about both design and functionality. They go to the cinema, but mainly arthouse and foreign. They visit the theatre and art galleries. They care about their coffee and the making of it might even be described as a ritual. They have separate grinders and espresso machines and are especially particular about everything to do with coffee - the beans (where they come from and how they are roasted), the grind, the making of the coffee itself, right down to the cups and glasses in which they are served.

Industry/Entity Type

Construction

Requirements
Must have
• A look and feel of premiumness without being staid. I think companies that have done this incredible well include Velmor, Quiso, Tavrel, Dorfu, KTZ. They are clearly premium, but have a feeling of what I describe as understated cutting edge about them. There is a lot of work that has gone into all of their graphic material yet they don't look "try hard".The colour palate is quite narrow - black, white, silver/chrome, and various coffee shades ranging perhaps from the golden brown of the crema to the rich dark brown of a roasted bean.
Nice to have
• I would like the coffee bag to be something that people leave out because it looks cool an chic.
Should not have
• Please avoid the cliches. I was thrilled with the creativity in the logo work, so I am enthusiastic at the prospect of seeing the same here.

Importantly, please avoid steaming cups at all costs! Also, pictures of people sipping coffee and looking blissfully content are not what I'm looking for.

Also, out emphasis is italian style coffee - espresso, late etc rather than the long black coffee that comes out of a filter machine that is popular in the US - consequently images that connote that should be avoided.

```html
<!DOCTYPE html>
<html lang="en">
<head>
<meta charset="utf-8">
<title>Brewvantia Variety Labels</title>
<link rel="stylesheet" href="https://fonts.googleapis.com/css2?family=Questrial&display=swap">
<style>
  :root {
    --kraft: #bfb39d;
    --kraft-light: #c9bea9;
    --kraft-dark: #b3a68e;
    --roast-dark: #2a140b;
    --roast-dark-edge: #1c0c05;
    --roast-mid: #5a2d12;
    --roast-mid-edge: #4a230c;
    --cream: #f3e6d2;
    --cream-line: #e8d3b4;
    --decaf-text: #b8937a;
    --decaf-line: #c9a98e;
    --organic-green: #93a452;
  }
  * { box-sizing: border-box; margin: 0; padding: 0; }
  html, body {
    width: 1200px;
    height: 900px;
    overflow: hidden;
  }
  body {
    position: relative;
    background: radial-gradient(ellipse at 45% 40%, var(--kraft-light) 0%, var(--kraft) 55%, var(--kraft-dark) 100%);
    font-family: "Questrial", "Century Gothic", sans-serif;
  }
  .label {
    position: absolute;
    height: 79px;
    border-radius: 12px;
    padding: 5px;
    border: 2px solid var(--roast-mid-edge);
    background: var(--roast-mid);
    box-shadow: 0 1px 2px rgba(40, 20, 5, 0.25);
  }
  .label-inner {
    width: 100%;
    height: 100%;
    border-radius: 8px;
    border: 1.5px solid var(--cream-line);
    display: flex;
    flex-direction: column;
    align-items: center;
    justify-content: center;
    text-align: center;
    color: var(--cream);
    font-size: 23px;
    line-height: 1.1;
  }
  .label--single-origin {
    background: var(--roast-dark);
    border-color: var(--roast-dark-edge);
  }
  .label--single-origin .label-inner { border-color: var(--cream); }
  .label--specialty .label-inner {
    border-color: var(--decaf-line);
    color: var(--decaf-text);
  }
  .label--specialty .label-inner.organic { color: var(--organic-green); }
  .label-inner.long { font-size: 19px; }
  .variety-sub { font-size: 18px; margin-top: 2px; }

  .col-origin { left: 72px; width: 298px; }
  .col-house { left: 447px; width: 298px; }
  .col-specialty { left: 825px; width: 303px; }
  .row-1 { top: 228px; }
  .row-2 { top: 348px; }
  .row-3 { top: 468px; }
  .row-4 { top: 591px; }
</style>
</head>
<body>
  <main class="label-sheet">
    <section class="family family--single-origin">
      <div class="label label--single-origin col-origin row-1"><div class="label-inner">Ethiopian Garsu</div></div>
      <div class="label label--single-origin col-origin row-2"><div class="label-inner">Costa Rica El Pinar</div></div>
      <div class="label label--single-origin col-origin row-3"><div class="label-inner long">Nicaraguan Tolvanera<br>Superior</div></div>
    </section>

    <section class="family family--house-blends">
      <div class="label label--house col-house row-1"><div class="label-inner">The Keystone</div></div>
      <div class="label label--house col-house row-2"><div class="label-inner">The Sybarite</div></div>
      <div class="label label--house col-house row-3"><div class="label-inner">The Devotee</div></div>
      <div class="label label--house col-house row-4"><div class="label-inner">The Reveller</div></div>
    </section>

    <section class="family family--specialty">
      <div class="label label--specialty col-specialty row-1"><div class="label-inner organic">Fair Trade Organic</div></div>
      <div class="label label--specialty col-specialty row-2"><div class="label-inner">Mexican Mountain<span class="variety-sub">Decafeinated</span></div></div>
      <div class="label label--specialty col-specialty row-3"><div class="label-inner">Swiss Decafeinated</div></div>
      <div class="label label--specialty col-specialty row-4"><div class="label-inner">Swiss Decafeinated</div></div>
    </section>
  </main>
</body>
</html>
```